Web design for facial expression recognition service

We offer a service which allows customers to film large panels of participants looking at some video/screen (e.g. an advertisement) and to analyze the facial expressions shown by the participants. We are looking for the design of a new website which will make it easy for our customers to setup and view the results of these experiments online.
Competitor's websites that may serve as a reference are:
http://www.moravint.com/tessly/#pane_overview
http://www.brondupix.com/homepage.aspx
https://www.kaplomo.com/
The website will (for as far as the design is concerned) consist of three parts:
- A public home page (and perhaps some contact/news/about page), designed to catch the attention/interest potential customers.
- A (protected) project result page, showing the results in an interactive page with charts and numerical data.
- Pages (also protected) with fields and tables (setting up the project details).
The winner of this design project should provide us with at least one design for each of the above in order to get a complete 'theme' going which our developers can use. However, you are welcome to initially only provide the design for the project result page and/or home page.
We are looking for a modern, fresh, yet professional look (my client is a more established party in the field).
The final delivery should consist of layered Photoshop or Illustrator files.
Thank you in advance for participating!
Updates
Dear designers,
Reason: Extending the deadline by a few days to give designers a chance to submit designs for the other pages and process further feedback.
Target Market(s)
marketing research agencies (B2B service)
Industry/Entity Type
Delivery
Requirements
Must have
- Home page:
- Basic advertisement of the service; some quick explanation of how it works
- A way to login for existing users
- A link/button/banner inviting people to sign up
- Navigation controls to 2-3 other pages
- Social media links (Frendo, LinkedIn group)
- Company logo (sorry, can't provide it as my client wishes to remain anonymous for now, but it's rounded and has blue as it's main color).
- Copyright / creator details
Project result page:
(see attachment 1 for a functional mockup - the design may follow this layout closely, or be completely different)
- Title
- A video player and basic numerical data
- Different views of the analysis results can dynamically be added/removed/collapsed/expanded; each one of these views will show some kind of chart, filters (combos), numerical data and a download button/link.
- A way to sign out, go to the main project page and go to the main page
- Logo
- Copyright
The form pages:
(see attachment 2 for a functional mockup of one of the pages; feel free to change some elements to better show the overall style)
- Title
- Text fields, combos, calendar pickers, tables, navigation links
- Logo
- Copyright
Nice to have
- Any creative text elements or product logo/symbol are a bonus. However, the basic "Lorem Ipsum" would do too.

```html
<!DOCTYPE html>
<html lang="en">
<head>
<meta charset="utf-8">
<title>Company Name — Facial expression measurement</title>
<link href="https://fonts.googleapis.com/css2?family=Ubuntu:wght@400;500;700&family=Open+Sans:wght@600;700&display=swap" rel="stylesheet">
<style>
:root{
  --brand-blue:#1b83be;
  --brand-blue-light:#2aa3d8;
  --header-bg:#2e2e2e;
  --footer-bg:#595959;
  --ink:#2b2b2b;
  --body-text:#3a3a3a;
  --white:#ffffff;
  --band-grey:#e4e4e4;
}
*{margin:0;padding:0;box-sizing:border-box}
html,body{width:978px;height:1200px;overflow:hidden;background:var(--white)}
body{position:relative;font-family:Arial,Helvetica,sans-serif;color:var(--body-text)}
.abs{position:absolute}

/* header */
.site-header{left:0;top:0;width:978px;height:68px;background:var(--header-bg)}
.logo-dot{left:106px;top:8px;width:52px;height:52px;border-radius:50%;background:var(--brand-blue)}
.logo-name{left:171px;top:22px;font-family:Ubuntu,sans-serif;font-weight:500;font-size:21px;color:var(--white)}
.main-nav a{position:absolute;top:29px;height:25px;line-height:25px;font-size:11px;font-weight:bold;color:var(--white);text-decoration:none}
.main-nav a.active{background:linear-gradient(#2aa6dc,#1b83be);padding:0 8px;left:442px;width:74px;text-align:center}

/* hero */
.hero{left:0;top:68px;width:978px;height:344px;background:linear-gradient(90deg,#5d7a4c 0%,#7a8d66 25%,#b4b8b3 48%,#c9ccce 70%,#a9aeb0 100%)}
.hero-band{left:0;top:383px;width:978px;height:29px;background:linear-gradient(#3c3c3c,#5a5a5a)}
.hero-title{left:103px;top:128px;font-family:Ubuntu,sans-serif;font-weight:700;font-size:37px;color:var(--brand-blue-light);letter-spacing:-0.5px;white-space:nowrap}
.hero-text{left:105px;top:178px;font-family:Ubuntu,sans-serif;font-size:20.4px;line-height:23.6px;color:var(--white);white-space:nowrap}
.demo-button{left:105px;top:287px;width:186px;height:64px;border-radius:9px;background:linear-gradient(#ffffff,#d6d6d6 70%,#bdbdbd);font-family:Ubuntu,sans-serif;color:var(--ink);text-decoration:none}
.demo-button .small{position:absolute;left:12px;top:4px;font-size:20px;letter-spacing:1px;color:#444}
.demo-button .big{position:absolute;left:39px;top:26px;font-size:33px;font-weight:700;letter-spacing:1px}
.demo-button .arrow{position:absolute;left:146px;top:37px}

.laptop-frame{left:437px;top:109px;width:392px;height:260px;border-radius:12px 12px 0 0;background:#1d1d1d;border:2px solid #bfbfbf}
.laptop-screen{left:454px;top:127px;width:359px;height:226px;background:linear-gradient(90deg,#d7ecfb 0%,#a9d4f3 55%,#6fa9d6 100%)}
.laptop-base{left:371px;top:367px;width:523px;height:20px;border-radius:2px 2px 10px 10px;background:linear-gradient(#f2f2f2,#b8b8b8)}
.screen-text{left:465px;top:155px;font-family:'Open Sans',sans-serif;font-weight:600;font-size:23px;line-height:27.5px;color:#1c6fa6;white-space:nowrap}
.play{left:590px;top:222px}

/* emotions */
.section-title{left:0;width:978px;text-align:center;font-family:'Open Sans',sans-serif;font-weight:700;color:var(--ink)}
.emotions-bg{left:0;top:632px;width:978px;height:132px;background:linear-gradient(#ffffff,var(--band-grey))}
.portrait{width:139px;height:139px;border-radius:50%;border:4px solid #4a4a4a;top:493px}
.feature-title{width:250px;text-align:center;font-family:'Open Sans',sans-serif;font-weight:600;font-size:23px;color:var(--brand-blue)}
.feature-text{font-size:12.2px;line-height:14.7px;color:var(--body-text);white-space:nowrap}

/* research */
.research-title{font-family:'Open Sans',sans-serif;font-weight:600;font-size:22px;color:var(--brand-blue);white-space:nowrap}
.quote-mark{font-family:Georgia,serif;font-size:30px;color:var(--brand-blue);font-style:italic}
.research-text{font-size:11.8px;line-height:16.3px;color:#2d2d2d;white-space:nowrap}
.read-more{font-size:11.4px;font-weight:bold;color:#2d2d2d;text-decoration:none}

/* partners */
.partners{left:0;top:1049px;width:978px;height:82px;background:linear-gradient(#e9e9e9,#ffffff 14%)}
.partner{top:1080px;font-family:Arial,Helvetica,sans-serif;font-weight:bold;font-size:14px;color:#333;display:flex;align-items:center;gap:5px;transform:translateX(-50%);white-space:nowrap}
.partner i{display:inline-block;width:10px;height:10px;background:#333}

/* footer */
.site-footer{left:0;top:1131px;width:978px;height:69px;background:var(--footer-bg)}
.footer-nav{left:102px;font-size:11px;font-weight:bold;color:var(--white);word-spacing:2px;white-space:nowrap}
.copyright{left:102px;font-family:Ubuntu,sans-serif;font-size:10.5px;color:#e6e6e6}
.social{width:30px;height:30px;border-radius:50%;background:radial-gradient(circle at 40% 35%,#8a8a8a,#4a4a4a);color:var(--white);font-size:6.5px;font-weight:bold;text-align:center;line-height:30px}
</style>
</head>
<body>

<header class="abs site-header">
  <div class="abs logo-dot" aria-hidden="true"></div>
  <div class="abs logo-name">Company Name</div>
  <nav class="main-nav">
    <a class="active" href="#">Homepage</a>
    <a href="#" style="left:548px">Clients</a>
    <a href="#" style="left:627px">Press</a>
    <a href="#" style="left:699px">Team</a>
    <a href="#" style="left:769px">Jobs</a>
    <a href="#" style="left:836px">Contact Us</a>
  </nav>
</header>

<section>
  <div class="abs hero" role="img" aria-label="Soft blurred office background with greenery"></div>
  <div class="abs hero-band"></div>
  <h1 class="abs hero-title">Using webcams</h1>
  <p class="abs hero-text">we can read how hundreds of<br>people really feel about your<br>video ads in less than two<br>days!</p>
  <a class="abs demo-button" href="#">
    <span class="small">Requeat to</span>
    <span class="big">Demo</span>
    <svg class="arrow" width="24" height="24" viewBox="0 0 24 24" aria-hidden="true"><circle cx="12" cy="12" r="12" fill="#222"/><path d="M9 6l7 6-7 6" fill="none" stroke="#fff" stroke-width="3"/></svg>
  </a>
  <div class="abs laptop-frame"></div>
  <div class="abs laptop-screen" role="img" aria-label="Laptop screen showing a wireframe face scan"></div>
  <div class="abs laptop-base"></div>
  <p class="abs screen-text">Facial Expression<br>measurement for<br>video ads.</p>
  <svg class="abs play" width="68" height="49" viewBox="0 0 68 49" aria-hidden="true"><rect width="68" height="49" fill="#3b3b3b"/><path d="M26 11l20 13.5L26 38z" fill="#fff"/></svg>
</section>

<section>
  <div class="abs emotions-bg"></div>
  <h2 class="abs section-title" style="top:432px;font-size:25px">Company Measures A Range Of Emotions</h2>

  <div class="abs portrait" style="left:144px;background:radial-gradient(#e2b49a,#b57d62)" role="img" aria-label="Face with tracking points"></div>
  <div class="abs portrait" style="left:422px;background:radial-gradient(#d9a688,#3b6aa8)" role="img" aria-label="Smiling man"></div>
  <div class="abs portrait" style="left:695px;background:radial-gradient(#e8c9b6,#c7a591)" role="img" aria-label="Woman with headphones"></div>

  <h3 class="abs feature-title" style="left:89px;top:645px">How It Works</h3>
  <h3 class="abs feature-title" style="left:373px;top:645px">Facial Expression</h3>
  <h3 class="abs feature-title" style="left:643px;top:645px">Recognition</h3>

  <p class="abs feature-text" style="left:121px;top:684px">Brondupix is a technology firm that<br>uses computer vision to read pe-<br>ople's faces and to measure what<br>emotions they're feeling.</p>
  <p class="abs feature-text" style="left:400px;top:684px">Brondupix is a technology firm that<br>uses computer vision to read pe-<br>ople's faces and to measure what<br>emotions they're feeling.</p>
  <p class="abs feature-text" style="left:668px;top:680px">Brondupix is a technology firm that<br>uses computer vision to read pe-<br>ople's faces and to measure what<br>emotions they're feeling.</p>
</section>

<section>
  <h2 class="abs section-title" style="top:776px;font-size:26px">A perfect research solution for...</h2>

  <h3 class="abs research-title" style="left:106px;top:844px">Agile Feedback</h3>
  <span class="abs quote-mark" style="left:84px;top:872px">“</span>
  <p class="abs research-text" style="left:106px;top:884px">Quisque gravida felis eu massa consecte-<br>tur at malesuada nibh porttitor. Nam nunc<br>nulla, tempus at viverr sit ametet semper<br>nec diamhasellus tellus elit, placerat eu<br>massa consectetur at malesuada nibh<br>porttitor. Nam nunc nulla, tempus at viverr<br>sit ametet.</p>
  <a class="abs read-more" href="#" style="left:105px;top:1011px">Read More &gt;&gt;</a>

  <h3 class="abs research-title" style="left:384px;top:845px">Market Research</h3>
  <span class="abs quote-mark" style="left:363px;top:872px">“</span>
  <p class="abs research-text" style="left:383px;top:884px">Quisque gravida felis eu massa consectetur<br>at malesuada nibh porttitor. Nam nunc nulla,<br>tempus at viverr sit ametet semper nec diam-<br>hasellus tellus elit, placerat eu massa con-<br>sectetur at malesuada nibh porttitor. Nam<br>nunc nulla,</p>
  <a class="abs read-more" href="#" style="left:382px;top:992px">Read More &gt;&gt;</a>

  <h3 class="abs research-title" style="left:662px;top:847px">Usability Testing</h3>
  <span class="abs quote-mark" style="left:645px;top:872px">“</span>
  <p class="abs research-text" style="left:664px;top:884px">Quisque gravida felis eu massa consec-<br>tetur at malesuada nibh porttitor. Nam<br>nunc nulla, tempus at viverr sit ametet<br>semper nec diamhasellus tellus elit, pla-<br>cerat.</p>
  <a class="abs read-more" href="#" style="left:654px;top:988px">Read More &gt;&gt;</a>
</section>

<section>
  <div class="abs partners"></div>
  <div class="abs partner" style="left:152px">Sonari</div>
  <div class="abs partner" style="left:266px"><i></i>Reelhaus</div>
  <div class="abs partner" style="left:380px">Bidora</div>
  <div class="abs partner" style="left:475px">Omnivale</div>
  <div class="abs partner" style="left:570px"><i></i>The Ledgerist</div>
  <div class="abs partner" style="left:689px">Norvik</div>
  <div class="abs partner" style="left:806px"><i></i>Hemvo</div>
</section>

<footer class="abs site-footer">
  <div class="abs footer-nav" style="top:12px">Homepage &nbsp;| &nbsp;Clients &nbsp;| &nbsp;Press &nbsp;| &nbsp;Team &nbsp;| &nbsp;Jobs &nbsp;| &nbsp;Contact Us</div>
  <div class="abs copyright" style="top:36px">© 2012-2013Company name, Inc. All rights reserved.</div>
  <div class="abs social" style="left:776px;top:19px">Feed</div>
  <div class="abs social" style="left:815px;top:19px">Chirpa</div>
  <div class="abs social" style="left:853px;top:19px">Frendo</div>
</footer>

</body>
</html>
```